Book-my-Mentor-Berlin Club

I would like an envelope that I give to companies or customers in order to draw attention to a birthday, loyalty or celebration. The cover should be based on the homepage / www.book-my-mentor-berlin.example (colors and design).

with sporty greetings, Florian Haberkorn
book my mentor berlin
Kastanien Str. 41
10439 Berlin

```html
<!DOCTYPE html>
<html lang="en">
<head>
<meta charset="utf-8">
<title>Book-my-Mentor-Berlin Club – Envelope</title>
<link rel="stylesheet" href="https://fonts.googleapis.com/css2?family=Archivo:wght@400;700&family=Roboto+Condensed:wght@400&family=Yellowtail&display=swap">
<style>
  :root {
    --bg-top: #c0dfc8;
    --bg-mid: #f5f3cd;
    --bg-bottom: #f1c9d8;
    --envelope: #0c0c0d;
    --flap: #e54a35;
    --flap-text: #f6e2de;
    --ink: #ffffff;
  }
  * { box-sizing: border-box; margin: 0; padding: 0; }
  html, body { width: 1200px; height: 800px; overflow: hidden; }
  body {
    background: linear-gradient(180deg, var(--bg-top) 0%, var(--bg-mid) 45%, var(--bg-bottom) 100%);
    font-family: "Archivo", Arial, sans-serif;
    position: relative;
  }
  .envelope {
    position: absolute;
    width: 520px;
    height: 260px;
    background: var(--envelope);
    color: var(--ink);
    box-shadow: 0 12px 30px rgba(0,0,0,0.18);
  }
  .envelope--back { left: 90px; top: 110px; }
  .envelope--front { left: 590px; top: 430px; }

  .flap { position: absolute; left: 0; top: 0; width: 100%; height: 48px; display: block; }
  .flap__label {
    position: absolute; left: 0; right: 40px; top: 15px;
    text-align: center;
    font-weight: 700;
    font-size: 15px;
    color: var(--flap-text);
    white-space: nowrap;
  }

  .club-title {
    position: absolute;
    font-weight: 700;
    font-size: 21px;
    white-space: nowrap;
  }
  .envelope--back .club-title { right: 40px; top: 76px; }
  .envelope--front .club-title { left: 36px; top: 132px; }

  .club-mark {
    position: absolute;
    display: flex; align-items: center; gap: 8px;
    font-weight: 700;
    font-size: 11px; white-space: nowrap;
  }
  .club-mark__dot {
    width: 14px; height: 14px; border-radius: 50%;
    background: var(--ink);
  }
  .envelope--back .club-mark { right: 40px; top: 128px; }
  .envelope--front .club-mark { left: 130px; top: 184px; }

  .sender {
    position: absolute;
    font-style: normal;
    line-height: 1.15;
  }
  .envelope--back .sender { left: 28px; bottom: 20px; }
  .envelope--front .sender { right: 24px; top: 28px; text-align: right; }
  .sender__greeting {
    font-family: "Roboto Condensed", Arial, sans-serif;
    font-size: 9px;
  }
  .sender__name {
    font-family: "Yellowtail", cursive;
    font-size: 27px; line-height: 1.05;
  }
  .sender__line { font-size: 12px; }
</style>
</head>
<body>

<section class="envelope envelope--back" aria-label="Envelope back with flap">
  <svg class="flap" viewBox="0 0 520 48" preserveAspectRatio="none" aria-hidden="true">
    <path d="M0 0 H500 L520 14 V30 L470 48 H36 Q22 48 14 40 Z" fill="var(--flap)"/>
  </svg>
  <div class="flap__label">Book-my-Mentor-Berlin Club</div>

  <div class="club-title">Book-my-Mentor-Berlin Club</div>

  <div class="club-mark"><span class="club-mark__dot"></span>Book-my-Mentor-Berlin Club</div>

  <address class="sender">
    <div class="sender__greeting">with sporty greetings,</div>
    <div class="sender__name">Florian Haberkorn</div>
    <div class="sender__line">book my mentor berlin</div>
    <div class="sender__line">Kastanien Str. 41</div>
    <div class="sender__line">10439 Berlin</div>
  </address>
</section>

<section class="envelope envelope--front" aria-label="Envelope front">
  <div class="club-title">Book-my-Mentor-Berlin Club</div>

  <div class="club-mark"><span class="club-mark__dot"></span>Book-my-Mentor-Berlin Club</div>

  <address class="sender">
    <div class="sender__greeting">with sporty greetings,</div>
    <div class="sender__name">Florian Haberkorn</div>
    <div class="sender__line">book my mentor berlin</div>
    <div class="sender__line">Kastanien Str. 41</div>
    <div class="sender__line">10439 Berlin</div>
  </address>
</section>

</body>
</html>
```